Marlo Tidy Yard Website

We need a website design for this new company. I've attached the company logo. This company is in the construction industry that provides general labor, maintenance and cleaning for construction sites. We want a clean and simple website that can be easy to navigate.

Target Market(s)

Construction industry

Industry/Entity Type

Construction

Number of Pages Required

2 page

Font styles to use
Sans Serif

```html
<!DOCTYPE html>
<html lang="en">
<head>
<meta charset="utf-8">
<title>Marlo Tidy Yard</title>
<link href="https://fonts.googleapis.com/css2?family=Archivo:wght@700;800;900&family=Jost:wght@400;500&display=swap" rel="stylesheet">
<style>
:root{
  --navy:#0b0a6e;
  --navy-deep:#07066a;
  --orange:#ff6a00;
  --ink:#333333;
  --muted:#555555;
  --band:#f2f2f2;
  --line:#cccccc;
  --white:#ffffff;
  --hero-dark:#3a3a3a;
}
*{margin:0;padding:0;box-sizing:border-box}
html,body{width:1200px;height:2299px;overflow:hidden;background:var(--white)}
body{position:relative;font-family:"Jost",sans-serif;color:var(--ink)}
.abs{position:absolute}
.heading{font-family:"Archivo",sans-serif;font-weight:800;color:var(--navy);font-size:31px;letter-spacing:.5px;text-align:center;width:100%;left:0}
.heading .accent{color:var(--orange)}
.rule{left:512px;width:176px;height:2px;background:var(--line)}
.lede{width:100%;left:0;text-align:center;font-size:16.5px;color:var(--ink)}

/* header */
.brand{left:142px;top:28px;font-family:"Archivo",sans-serif;font-weight:900;font-size:26px;color:var(--navy);line-height:1.05;letter-spacing:.3px}
.contact-email{left:578px;top:31px;display:flex;align-items:center;gap:14px}
.contact-email .icon{width:40px;height:40px;border:2px solid var(--orange);border-radius:50%;display:flex;align-items:center;justify-content:center}
.contact-email .label{font-size:14px;color:var(--muted);line-height:1.35}
.contact-email .label a{color:var(--orange);text-decoration:none;display:block}
.phone-box{left:814px;top:34px;width:159px;height:35px;background:var(--navy);border-radius:3px;display:flex;align-items:center;gap:14px;padding-left:14px;color:var(--white);font-size:16.5px}
.menu-btn{left:1018px;top:32px;width:40px;height:40px;border-radius:50%;background:var(--orange);display:flex;align-items:center;justify-content:center}

/* hero */
.hero{left:0;top:103px;width:1200px;height:493px;background:linear-gradient(90deg,#8a8f86 0%,#a6a89d 35%,#c9c7c0 58%,#ececea 70%,#f0f0f0 100%)}
.hero-badge{left:726px;top:191px;width:316px;height:316px;border-radius:50%;background:var(--hero-dark);display:flex;flex-direction:column;align-items:center;justify-content:center;text-align:center}
.hero-badge .mark{font-family:"Archivo",sans-serif;font-weight:900;font-size:26px;color:#555555;margin-bottom:22px;margin-top:-20px}
.hero-badge .tag{font-family:"Archivo",sans-serif;font-weight:700;color:var(--white);font-size:21px;line-height:1.6;letter-spacing:.3px}

/* services */
.service{width:330px;text-align:center}
.service .ring{width:206px;height:206px;border-radius:50%;background:var(--white);box-shadow:0 0 0 1px #ececec,0 2px 6px rgba(0,0,0,.08);margin:0 auto;display:flex;align-items:center;justify-content:center}
.service .photo{width:194px;height:194px;border-radius:50%}
.service h3{font-family:"Jost",sans-serif;font-weight:500;color:var(--navy);font-size:19px;margin-top:26px;letter-spacing:.3px}
.service p{font-size:14px;line-height:20px;color:var(--ink);margin-top:12px}

/* about */
.about-band{left:0;top:1197px;width:1200px;height:567px;background:var(--band)}
.about-copy{left:142px;top:1375px;width:450px}
.about-copy h4{font-family:"Jost",sans-serif;font-weight:500;color:var(--navy);font-size:17.5px;line-height:23px}
.about-copy p{font-size:13.6px;line-height:20px;color:var(--ink);margin-top:14px}
.about-copy p + p{margin-top:12px}
.btn{left:139px;top:1628px;width:97px;height:30px;background:var(--orange);color:var(--white);font-size:14.5px;display:flex;align-items:center;justify-content:center;box-shadow:2px 2px 0 #d8d8d8}
.about-frame{left:625px;top:1376px;width:432px;height:295px;background:var(--white);padding:9px;box-shadow:0 1px 6px rgba(0,0,0,.1)}
.about-frame .photo{width:100%;height:100%;background:linear-gradient(180deg,#cfd8d2 0%,#c7c8b8 40%,#e0784a 62%,#d86a3e 80%,#7e9a5e 100%)}

/* clients */
.client{width:213px;height:100px;background:var(--white);box-shadow:0 1px 6px rgba(0,0,0,.12);display:flex;align-items:center;justify-content:center;gap:10px;font-family:"Archivo",sans-serif;font-weight:800;font-size:22px;color:var(--navy)}
.client .dot{width:16px;height:16px;border-radius:50%;background:var(--navy)}
.arrow{width:24px;height:24px;border-radius:50%;border:1px solid #dddddd;display:flex;align-items:center;justify-content:center}

/* footer */
.footer{left:0;top:2136px;width:1200px;height:163px;background:var(--navy-deep)}
.footer-mark{left:146px;top:2188px;font-family:"Archivo",sans-serif;font-weight:900;font-size:44px;line-height:1.05;color:#3d3da0}
.footer-info{right:143px;top:2168px;text-align:right;color:var(--white);font-size:12px}
.footer-info nav a{color:var(--white);text-decoration:none}
.footer-info nav .sep{color:#6b6bb0;margin:0 16px}
.footer-info .row{margin-top:16px;display:flex;justify-content:flex-end;align-items:center;gap:8px}
.footer-info .row .sep{color:#6b6bb0;margin:0 8px}
.footer-info .copy{margin-top:14px}
</style>
</head>
<body>

<header>
  <div class="abs brand">MARLO<br>TIDY YARD</div>
  <div class="abs contact-email">
    <span class="icon">
      <svg width="18" height="14" viewBox="0 0 18 14"><rect x="1" y="1" width="16" height="12" fill="none" stroke="#0b0a6e" stroke-width="1.5"/><path d="M1 1 L9 8 L17 1" fill="none" stroke="#0b0a6e" stroke-width="1.5"/></svg>
    </span>
    <span class="label">Email Us On:<a href="#">info@marlotidyyard.com</a></span>
  </div>
  <div class="abs phone-box">
    <svg width="12" height="20" viewBox="0 0 12 20"><rect x="1" y="1" width="10" height="18" rx="2" fill="none" stroke="#fff" stroke-width="1.5"/><circle cx="6" cy="16" r="1" fill="#fff"/></svg>
    <span>555-010-2040</span>
  </div>
  <div class="abs menu-btn">
    <svg width="16" height="13" viewBox="0 0 16 13"><rect y="0" width="16" height="2" fill="#fff"/><rect y="5.5" width="16" height="2" fill="#fff"/><rect y="11" width="16" height="2" fill="#fff"/></svg>
  </div>
</header>

<section>
  <div class="abs hero" role="img" aria-label="Worker in hard hat sweeping a paved walkway at a construction site"></div>
  <div class="abs hero-badge">
    <div class="mark">MARLO TIDY YARD</div>
    <div class="tag">DON'T STRESS WE'LL<br>HANDLE THE MESS</div>
  </div>
</section>

<section>
  <h2 class="abs heading" style="top:674px">OUR SERVICES</h2>
  <div class="abs rule" style="top:716px"></div>
  <p class="abs lede" style="top:744px">Lorem ipsum dolor sit amet, consectetuer adipiscing elit, sed diam nonummy nibh</p>

  <div class="abs service" style="left:102px;top:806px">
    <div class="ring"><div class="photo" role="img" aria-label="Crew of labourers in orange safety gear working on site" style="background:linear-gradient(160deg,#8d9197,#c46a3a 55%,#6f6a62)"></div></div>
    <h3>GENERAL LABOR</h3>
    <p>Lorem ipsum dolor sit amet, consectetuer<br>adipiscing elit, sed diamond cutpo</p>
  </div>
  <div class="abs service" style="left:433px;top:806px">
    <div class="ring"><div class="photo" role="img" aria-label="Worker in hard hat laying paving stones, orange overlay" style="background:radial-gradient(circle at 50% 40%,#ff8a3a,#e95f10 70%,#c85010)"></div></div>
    <h3>MAINTENANCE</h3>
    <p>Lorem ipsum dolor sit amet, consectetuer<br>adipiscing elit, sed diamond cutpo</p>
  </div>
  <div class="abs service" style="left:764px;top:806px">
    <div class="ring"><div class="photo" role="img" aria-label="Worker in yellow hard hat cleaning a stone surface" style="background:linear-gradient(150deg,#7b7f86,#505a6e 50%,#9a9a96)"></div></div>
    <h3>CLEANING</h3>
    <p>Lorem ipsum dolor sit amet, consectetuer<br>adipiscing elit, sed diamond cutpo</p>
  </div>
</section>

<section>
  <div class="abs about-band"></div>
  <h2 class="abs heading" style="top:1289px">ABOUT MARLO <span class="accent">TIDY YARD</span></h2>
  <div class="abs rule" style="top:1339px"></div>
  <div class="abs about-copy">
    <h4>Duis autem vel eum iriure dolor in hendrerit in vulputate velil esse molestie consequat, vel illum feugiat nulla facilisis</h4>
    <p>Lorem ipsum dolor sit amet, consectetuer adipiscing elit, sed diamond cutpowr nonummy nibh euismod tincidunt ut laoreet dolore magna aliquam eratmori volutpat. Ut wisi enim ad minim veniam, quis nostrud exerci tation ullamcorl suscipit lobortis nisl ut aliquip ex ea commodo consequat.</p>
    <p>At vero eros etnk accumsan et iusto odio dignissim quom facilisi. Duis autem vel eum iriure oli dolor in hendrerit in vulputate velil esse molestie consequat, vel illum meug more nulla facilisis. At vero eros etnk accumsan</p>
  </div>
  <a class="abs btn">Read More</a>
  <div class="abs about-frame"><div class="photo" role="img" aria-label="Smiling site supervisor in hard hat giving a thumbs up, holding plans"></div></div>
</section>

<section>
  <h2 class="abs heading" style="top:1842px">OUR CLIENTS</h2>
  <div class="abs rule" style="top:1886px"></div>
  <p class="abs lede" style="top:1904px">Lorem ipsum dolor sit amet, consectetuer adipiscing elit, sed diam nonummy nibh</p>

  <div class="abs arrow" style="left:83px;top:1994px"><svg width="6" height="10" viewBox="0 0 6 10"><path d="M5 1 L1 5 L5 9" fill="none" stroke="#bbb" stroke-width="1.3"/></svg></div>
  <div class="abs client" style="left:141px;top:1949px">Orbitline</div>
  <div class="abs client" style="left:377px;top:1949px">Skyvale</div>
  <div class="abs client" style="left:611px;top:1949px"><span class="dot"></span>Northgate Studio</div>
  <div class="abs client" style="left:846px;top:1949px">Greenfold</div>
  <div class="abs arrow" style="left:1096px;top:1994px"><svg width="6" height="10" viewBox="0 0 6 10"><path d="M1 1 L5 5 L1 9" fill="none" stroke="#bbb" stroke-width="1.3"/></svg></div>
</section>

<footer>
  <div class="abs footer"></div>
  <div class="abs footer-mark">MARLO<br>TIDY YARD</div>
  <div class="abs footer-info">
    <nav><a href="#">Home</a><span class="sep">|</span><a href="#">About Us</a><span class="sep">|</span><a href="#">Services</a><span class="sep">|</span><a href="#">Contact Us</a></nav>
    <div class="row">
      <span>48 Quarry Lane, Fenwick, AB 5521</span><span class="sep">|</span>
      <svg width="10" height="10" viewBox="0 0 10 10"><path d="M2 1 L4 1 L5 3 L4 4 Q5 6 6 6 L7 5 L9 6 L9 8 Q8 9 7 9 Q1 8 1 2 Q1 1 2 1Z" fill="#9a9ad0"/></svg>
      <span>555-010-2040</span><span class="sep">|</span>
      <svg width="11" height="8" viewBox="0 0 11 8"><rect width="11" height="8" fill="#9a9ad0"/><path d="M0 0 L5.5 4.5 L11 0" fill="none" stroke="#07066a" stroke-width="1"/></svg>
      <span>info@marlotidyyard.com</span>
    </div>
    <div class="copy">Copyright © 2019 Marlo Tidy Yard. All Rights Reserved.</div>
  </div>
</footer>

</body>
</html>
```